Mobile app for deals

Mobile App Name: Bid 2 Pact

Design screen shots for the issue of quotes for deals.

1. Loading screen
2. User signs in with credentials or signs up
2. Search by category
3. Search by location
4. Create a project

The expected experience after a project is placed:
- Project alerted
- Quotes
- Project complete
- Rating
- Payment

#TotallyExcited
Updates

Project Deadline Extended Reason: Deadline has been extended on request from a few designers who saw the project late and who would like to submit designs.Thank you to all who submitted on time, we are reviewing your designs and will respond shortly. Added Monday, June 29, 2015

Target Market(s)

Contractors market

Industry/Entity Type

Business Directory

Font styles to use
Sans Serif

Requirements
Must have
• Simple design
• User friendly
• Translateable (later)

```html
<!DOCTYPE html>
<html lang="en">
<head>
<meta charset="utf-8">
<title>Bid 2 Pact – Sign in</title>
<link rel="stylesheet" href="https://fonts.googleapis.com/css2?family=Exo+2:ital,wght@0,300;0,400;0,600;1,300;1,600&display=swap">
<style>
  :root {
    --page-bg: #e9ebee;
    --screen-blue: #0a5ca6;
    --line: rgba(255, 255, 255, 0.55);
    --line-soft: rgba(255, 255, 255, 0.3);
    --text: #ffffff;
    --text-muted: rgba(255, 255, 255, 0.8);
  }
  * { box-sizing: border-box; margin: 0; padding: 0; }
  html, body {
    width: 1200px;
    height: 1000px;
    overflow: hidden;
    background: var(--page-bg);
    font-family: "Exo 2", sans-serif;
  }
  .canvas {
    width: 1200px;
    height: 1000px;
    display: flex;
    align-items: center;
    justify-content: center;
  }
  .app-screen {
    position: relative;
    width: 507px;
    height: 900px;
    background: var(--screen-blue);
    color: var(--text);
    overflow: hidden;
  }
  .status-bar {
    position: absolute;
    top: 0; left: 0; right: 0;
    height: 32px;
    display: flex;
    align-items: center;
    justify-content: space-between;
    padding: 0 14px;
    font-size: 13px;
    font-weight: 600;
  }
  .status-bar .signal { display: flex; gap: 3px; }
  .status-bar .signal span {
    width: 6px; height: 6px; border-radius: 50%; background: var(--text);
  }
  .status-bar .battery { display: flex; align-items: center; gap: 5px; }
  .status-bar .battery-icon {
    width: 24px; height: 11px; border: 1px solid var(--text); border-radius: 2px; padding: 1px;
  }
  .status-bar .battery-icon::before {
    content: ""; display: block; width: 100%; height: 100%; background: var(--text);
  }
  .brand {
    position: absolute;
    top: 170px; left: 0; right: 0;
    display: flex;
    align-items: center;
    justify-content: center;
    gap: 12px;
  }
  .brand-dot {
    width: 34px; height: 34px; border-radius: 50%; border: 3px solid var(--text);
  }
  .brand-name {
    font-size: 28px;
    font-weight: 600;
    letter-spacing: 0.5px;
  }
  .sign-in-form {
    position: absolute;
    top: 300px;
    left: 50%;
    transform: translateX(-50%);
    width: 300px;
  }
  .field {
    position: relative;
    height: 56px;
    border-top: 1px solid var(--line-soft);
    border-bottom: 1px solid var(--line);
    display: flex;
    align-items: flex-end;
    padding: 0 4px 8px;
    margin-bottom: 22px;
    font-size: 21px;
    font-weight: 300;
    font-style: italic;
    color: var(--text-muted);
  }
  .submit-button {
    position: absolute;
    top: 555px;
    left: 50%;
    transform: translateX(-50%);
    width: 60px; height: 60px;
  }
  .social-register {
    position: absolute;
    left: 0; right: 0;
    top: 752px;
    border-top: 1px solid var(--line);
    height: 148px;
    display: flex;
    align-items: center;
    justify-content: center;
    font-size: 15px;
    font-style: italic;
    font-weight: 300;
    color: var(--text-muted);
  }
  .social-register strong {
    font-weight: 600;
    color: var(--text);
    margin-left: 5px;
  }
</style>
</head>
<body>
  <main class="canvas">
    <section class="app-screen">
      <header class="status-bar">
        <div class="signal"><span></span><span></span><span></span><span></span><span></span></div>
        <div class="clock">12:49 PM</div>
        <div class="battery">100% <span class="battery-icon"></span></div>
      </header>

      <div class="brand">
        <span class="brand-dot"></span>
        <span class="brand-name">Bid 2 Pact</span>
      </div>

      <form class="sign-in-form">
        <label class="field">E-mail</label>
        <label class="field">Password</label>
      </form>

      <svg class="submit-button" viewBox="0 0 60 60" aria-label="Sign in">
        <circle cx="30" cy="30" r="28" fill="none" stroke="#ffffff" stroke-width="1.3" stroke-opacity="0.8"/>
        <polyline points="26,20 36,30 26,40" fill="none" stroke="#ffffff" stroke-width="1.6"/>
      </svg>

      <footer class="social-register">register with<strong>Friendnet</strong></footer>
    </section>
  </main>
</body>
</html>
```